Clearpath Ledgers New Website

Please review the attached Design Brief with additional details. Thank you!

The goal is to create a website that effectively communicates the benefits of ClearPath Ledgers to eye care professionals. The website should streamline the process of understanding and utilizing ClearPath Ledgers' services, emphasizing improved patient outcomes, increased referrals, and enhanced patient engagement.

Target Market(s)

Eyecare Professionals

Number of Pages Required

4 page

```html
<!DOCTYPE html>
<html lang="en">
<head>
<meta charset="utf-8">
<title>Clearpath Ledgers</title>
<link href="https://fonts.googleapis.com/css2?family=Inter:wght@400;500;600;700;800&display=swap" rel="stylesheet">
<style>
:root{
  --blue:#1a62e6;
  --navy:#0e2f95;
  --ink:#1c2333;
  --muted:#6b7385;
  --soft:#eef4ff;
  --line:#dfe6f3;
  --orange:#f7a43a;
  --white:#ffffff;
}
*{box-sizing:border-box;margin:0;padding:0}
html,body{width:1200px;height:4428px;overflow:hidden}
body{position:relative;font-family:"Inter",sans-serif;color:var(--ink);background:var(--white)}
.abs{position:absolute}
.section{position:absolute;left:0;width:1200px}
.brand{display:flex;align-items:center;gap:10px;font-weight:700;font-size:26px;color:var(--navy)}
.brand-dot{width:18px;height:18px;border-radius:50%;background:var(--orange)}
.tagline{font-size:13px;color:var(--ink)}
/* header & hero */
.hero{top:0;height:713px;background:linear-gradient(180deg,#f2f7ff 0%,#e3edfc 100%)}
.nav{position:absolute;top:54px;display:flex;font-size:14px;font-weight:500}
.nav a{position:absolute;white-space:nowrap;color:var(--ink);text-decoration:none}
.nav a.active{color:var(--blue)}
.btn{display:flex;align-items:center;justify-content:center;font-weight:600;font-size:15px;border-radius:3px;text-decoration:none}
.btn-navy{background:var(--navy);color:var(--white)}
.btn-outline{border:1.5px solid var(--blue);color:var(--blue);background:var(--white)}
.btn-orange{background:var(--orange);color:var(--white)}
.hero-title{left:113px;top:228px;font-size:47px;font-weight:800;color:#11182b;letter-spacing:-.5px}
.hero-title span{color:var(--blue)}
.hero-band{left:103px;top:300px;width:312px;height:54px;background:var(--blue);border-radius:4px 14px 4px 14px;transform:skewX(-8deg)}
.hero-band-text{left:160px;top:300px;font-size:42px;font-weight:800;color:var(--white);line-height:54px}
.hero-sub{left:113px;top:376px;font-size:16px;font-weight:600;color:var(--navy)}
.hero-p{left:113px;top:406px;width:480px;font-size:13px;line-height:26px;color:var(--muted)}
.hero-art{left:567px;top:163px;width:633px;height:550px;border-radius:24px 0 0 0;background:linear-gradient(135deg,#ffffff 0%,#dbe7fb 60%,#c7d9f7 100%)}
/* headings */
.heading{width:1200px;text-align:center;font-size:28px;font-weight:700;color:#11182b}
.heading span{color:var(--blue);position:relative}
.heading span::after{content:"";position:absolute;left:8%;right:8%;bottom:-4px;height:3px;border-radius:3px;background:var(--orange)}
.lead{width:1200px;text-align:center;font-size:13px;line-height:26px;color:var(--muted)}
/* registry cards */
.reg-card{position:absolute;width:477px;height:157px;background:#fbfcff;border:1px solid var(--line);box-shadow:0 4px 14px rgba(30,70,150,.06)}
.reg-card.featured{border:2px solid var(--blue);background:var(--white)}
.reg-icon{position:absolute;left:36px;top:34px;width:86px;height:86px}
.reg-title{position:absolute;left:150px;top:24px;font-size:18px;font-weight:600;color:#11182b}
.reg-text{position:absolute;left:150px;top:57px;width:300px;font-size:13px;line-height:26px;color:var(--muted)}
.corner{position:absolute;right:0;bottom:0;width:34px;height:30px;background:var(--blue);clip-path:polygon(100% 0,100% 100%,0 100%,30% 0)}
/* blue band */
.band{top:1322px;height:352px;background:linear-gradient(100deg,#0a56d6 0%,#1468e6 60%,#0b51cf 100%);overflow:hidden}
.band-art{left:112px;top:45px;width:404px;height:258px;border-radius:8px;background:linear-gradient(160deg,#e7efff 0%,#9fbff2 55%,#1a3f8e 100%)}
.band-title{left:610px;top:110px;font-size:30px;font-weight:700;color:var(--white)}
.band-p{left:612px;top:162px;font-size:14px;color:#e4ecff}
/* construction */
.con-card{position:absolute;background:var(--white);border:1px solid var(--line);text-align:center}
.con-card.mid{border:2px solid var(--blue);box-shadow:0 10px 30px rgba(26,98,230,.15)}
.con-icon{position:absolute;left:50%;width:88px;height:88px;margin-left:-44px;border-radius:50%;background:var(--blue);border:5px solid #d6e4fd}
.con-title{position:absolute;left:0;width:100%;font-size:15px;font-weight:600;color:#11182b}
.con-text{position:absolute;left:26px;right:26px;font-size:13px;line-height:26px;color:#3a4255}
/* feedback */
.feedback{top:2350px;height:516px;background:linear-gradient(180deg,#e8f0fd 0%,#dde8fb 100%)}
.fb-card{position:absolute;top:199px;width:476px;height:244px;background:var(--white);clip-path:polygon(0 0,100% 0,100% 76%,86% 100%,0 100%)}
.fb-avatar{position:absolute;left:46px;top:26px;width:66px;height:66px;border-radius:50%;background:linear-gradient(135deg,#c9d6ea,#8aa3c8)}
.fb-name{position:absolute;left:141px;top:32px;font-size:17px;font-weight:600;color:#11182b}
.fb-role{position:absolute;left:141px;top:62px;font-size:13px;color:#a0a7b6}
.fb-quote{position:absolute;right:70px;top:22px;font-size:84px;font-weight:800;line-height:1;color:var(--blue);font-family:"Inter",sans-serif}
.fb-text{position:absolute;left:46px;top:118px;width:370px;font-size:13px;line-height:26px;color:#2a3142}
/* pricing */
.plan{position:absolute;top:3046px;width:310px;height:397px;background:#f8faff;border:1px solid var(--line);border-radius:6px;overflow:hidden}
.plan-head{position:absolute;left:0;top:0;width:100%;height:100px;clip-path:polygon(0 0,100% 0,100% 76%,0 100%)}
.plan-name{position:absolute;left:26px;top:34px;font-size:16px;font-weight:600;color:var(--white)}
.plan-price{position:absolute;right:20px;top:14px;font-size:36px;font-weight:700;color:var(--white)}
.plan-price sup{font-size:18px;vertical-align:14px;margin-right:4px}
.plan-tag{position:absolute;right:20px;top:60px;font-size:11px;background:var(--white);border-radius:10px;padding:1px 14px}
.plan ul{list-style:none;position:absolute;left:24px;top:139px}
.plan li{display:flex;align-items:center;gap:22px;height:43.5px;font-size:13px;color:var(--muted)}
.ok,.no{width:14px;height:14px;border-radius:50%;display:flex;align-items:center;justify-content:center}
.ok{background:#1fb05a}.no{background:#e5413b}
.plan .btn{position:absolute;left:32px;top:327px;width:240px;height:48px;border:1px solid #c9d5ec;border-radius:6px;background:var(--white);color:var(--blue)}
/* news */
.news{position:absolute;top:3708px;width:312px;height:311px;background:var(--white);border-radius:8px;box-shadow:0 6px 24px rgba(20,50,110,.09)}
.news-img{position:absolute;left:17px;top:17px;width:278px;height:143px;border-radius:4px}
.news-date{position:absolute;left:24px;top:176px;font-size:12px;color:var(--muted)}
.news-title{position:absolute;left:24px;top:202px;width:262px;font-size:16px;line-height:26px;font-weight:600;color:#11182b}
.news-more{position:absolute;left:24px;top:266px;display:flex;align-items:center;gap:12px;font-size:12px;font-weight:500;color:var(--blue)}
/* footer */
.footer{top:4091px;height:337px;background:linear-gradient(180deg,#f2f6fe 0%,#e9f0fd 100%)}
.f-head{position:absolute;top:64px;font-size:16px;font-weight:700;color:var(--navy)}
.f-links{position:absolute;top:104px;list-style:none;font-size:13px;color:var(--muted)}
.f-links li{height:34.5px}
</style>
</head>
<body>

<!-- Header & Hero -->
<section class="section hero">
  <div class="abs" style="left:112px;top:30px">
    <div class="brand"><span class="brand-dot"></span>Clearpath Ledgers</div>
    <div class="tagline" style="margin-top:6px;margin-left:6px">Empowering Healthcare</div>
  </div>
  <nav class="nav" style="left:0;top:54px">
    <a class="active" style="left:417px">About Us</a>
    <a style="left:508px">Services</a>
    <a style="left:596px">Pricing</a>
    <a style="left:670px">Testimonials</a>
    <a style="left:782px">Blog</a>
    <a style="left:838px">Contact</a>
    <a style="left:920px">FAQ</a>
  </nav>
  <a class="btn btn-navy abs" style="left:980px;top:41px;width:106px;height:42px;font-size:14px">Sign In</a>

  <h1 class="abs hero-title">Clinically <span>Actionable</span></h1>
  <div class="abs hero-band"></div>
  <div class="abs hero-band-text">Analytics</div>
  <p class="abs hero-sub">Track, Measure and Compare Your Clinical Outcomes</p>
  <p class="abs hero-p">The eye care industry's leading software designed to extract and analyze clinical outcomes from your EHR.</p>
  <a class="btn btn-navy abs" style="left:113px;top:493px;width:167px;height:44px">Start Free Trail</a>
  <a class="btn btn-outline abs" style="left:296px;top:493px;width:168px;height:44px">Learn More</a>

  <div class="abs hero-art" role="img" aria-label="Analytics dashboard with sales charts beside an illustrated clinician holding a large eye symbol"></div>
  <svg class="abs" style="left:585px;top:688px" width="30" height="20" viewBox="0 0 30 20"><path d="M9 5l6 6 6-6M9 11l6 6 6-6" fill="none" stroke="#1a62e6" stroke-width="2"/></svg>
</section>

<!-- Popular registries -->
<h2 class="abs heading" style="top:768px">Our Most <span>Popular</span> Registries</h2>
<p class="abs lead" style="top:823px">Lorem ipsumd olor sit, consectetu qsu some adipiscing elit eiusmod temp incididu nt utlabore<br>e dol magna great aliqua.mollit ani muim.</p>

<div class="reg-card" style="left:113px;top:921px">
  <svg class="reg-icon" viewBox="0 0 86 86"><path d="M43 6C30 28 16 42 16 58a27 27 0 0054 0C70 42 56 28 43 6z" fill="none" stroke="#1a62e6" stroke-width="3"/><circle cx="52" cy="54" r="12" fill="none" stroke="#1a62e6" stroke-width="3"/><circle cx="30" cy="64" r="5" fill="#f7a43a"/></svg>
  <div class="reg-title">Diabetes Management Registry</div>
  <p class="reg-text">This registry will enhance your care of diabetic patients by monitoring HbA1c change and predicting the advent of a retinopathy.</p>
</div>
<div class="reg-card featured" style="left:610px;top:921px">
  <svg class="reg-icon" viewBox="0 0 86 86"><rect x="14" y="18" width="58" height="50" rx="10" fill="none" stroke="#1a62e6" stroke-width="3"/><circle cx="43" cy="43" r="14" fill="none" stroke="#1a62e6" stroke-width="3"/><circle cx="43" cy="43" r="6" fill="#f7a43a"/></svg>
  <div class="reg-title">Cataract Extraction Registry</div>
  <p class="reg-text">Evaluating outcomes from cataract surgery is a very complex issue that involves many different factors.</p>
  <span class="corner"></span>
</div>
<div class="reg-card" style="left:113px;top:1104px">
  <svg class="reg-icon" viewBox="0 0 86 86"><path d="M8 48c18-24 52-24 70 0-18 24-52 24-70 0z" fill="none" stroke="#1a62e6" stroke-width="3"/><circle cx="43" cy="48" r="11" fill="none" stroke="#1a62e6" stroke-width="3"/><path d="M22 8l-6 14h8l-6 14M64 8l-6 14h8l-6 14" fill="none" stroke="#1a62e6" stroke-width="3"/></svg>
  <div class="reg-title">Dry Eye Registry</div>
  <p class="reg-text">This registry will guide you in prescribing the most effective treatment modalities for specific types of dry eye patients.</p>
</div>
<div class="reg-card" style="left:610px;top:1104px">
  <svg class="reg-icon" viewBox="0 0 86 86"><circle cx="40" cy="43" r="30" fill="none" stroke="#1a62e6" stroke-width="3"/><path d="M18 30c10-6 20 10 14 26M46 50l26 24" fill="none" stroke="#1a62e6" stroke-width="3"/></svg>
  <div class="reg-title">Myopia Registry</div>
  <p class="reg-text">Data driven reports from this registry, will guide you in prescribing the most efficacious modality of myopia management for each</p>
</div>

<!-- Blue band -->
<section class="section band">
  <svg class="abs" style="left:1040px;top:40px" width="160" height="240" viewBox="0 0 160 240"><path d="M160 0L50 100 160 240z" fill="#ffffff" opacity=".06"/></svg>
  <div class="abs band-art" role="img" aria-label="Illustrated presenter beside a large monitor showing bar and line charts"></div>
  <h2 class="abs band-title">It's Easy to Use!</h2>
  <p class="abs band-p">Data is automatically extracted.&nbsp; There's nothing for you to do.</p>
  <a class="btn btn-orange abs" style="left:610px;top:201px;width:200px;height:43px;font-size:15px;border-radius:2px">Start Free Trail Now</a>
</section>

<!-- Under construction -->
<h2 class="abs heading" style="top:1732px">Registries <span>Under</span> Construction</h2>
<p class="abs lead" style="top:1788px">Lorem ipsumd olor sit, consectetu qsu some adipiscing elit eiusmod temp incididu nt utlabore<br>e dol magna great aliqua.mollit ani muim.</p>
<svg class="abs" style="left:10px;top:1995px" width="130" height="60" viewBox="0 0 130 60"><path d="M0 58C40 30 80 18 130 10" fill="none" stroke="#c4d7fa" stroke-width="6" stroke-linecap="round"/></svg>
<svg class="abs" style="left:1068px;top:2120px" width="132" height="20" viewBox="0 0 132 20"><path d="M0 16L132 4" stroke="#b8d0fb" stroke-width="8"/></svg>

<div class="con-card" style="left:137px;top:1927px;width:306px;height:308px">
  <div class="con-icon" style="top:-30px"></div>
  <div class="con-title" style="top:86px">Quality Assessment Registry</div>
  <p class="con-text" style="top:120px">With the passage of the 21 st Century Cures Act, which deals with information blocking, payors will have access to all clinical, administrative and financial data that is contained in your certified EHR system.</p>
</div>
<div class="con-card mid" style="left:443px;top:1891px;width:314px;height:382px">
  <div class="con-icon" style="top:22px"></div>
  <div class="con-title" style="top:140px">OrthoK Registry</div>
  <p class="con-text" style="top:176px">ClearPath Ledgers can provide you with "real-time" clinical outcome data to help guide you in prescribing the most effective treatment to slow elongation.The data can also be used to enhance the financial viability of your</p>
  <span class="corner"></span>
</div>
<div class="con-card" style="left:757px;top:1927px;width:311px;height:308px">
  <div class="con-icon" style="top:-30px"></div>
  <div class="con-title" style="top:86px">AMD Registry</div>
  <p class="con-text" style="top:120px">Data driven reports from this registry, will guide you in prescribing the most efficacious treatment for each individual patient. You can also use this data as a tool to educate your patients, parents, educators and to market your practice.</p>
</div>

<!-- Feedback -->
<section class="section feedback">
  <h2 class="abs heading" style="top:58px">Explore <span>Clients</span> feedback</h2>
  <p class="abs lead" style="top:113px">Discover why users love our app. Read real-life experiences and see how our virtual<br>assistant is simplifying daily tasks.</p>
  <div class="fb-card" style="left:113px">
    <div class="fb-avatar"></div>
    <div class="fb-name">Maren Holt</div>
    <div class="fb-role">HR, Northfield Labs</div>
    <div class="fb-quote">”</div>
    <p class="fb-text">We're building a better application now, thanks to Healthcare. Sed perspiciatis unonis este natus error sit volutate accusantium dolor laudant totam rem aperiam eaupsa abillo inven veritatis</p>
  </div>
  <div class="fb-card" style="left:612px">
    <div class="fb-avatar"></div>
    <div class="fb-name">Tomas Reyes</div>
    <div class="fb-role">HR, Northfield Labs</div>
    <div class="fb-quote">”</div>
    <p class="fb-text">Great Service from a expert support system of Healthcare. Sed perspiciatis unonis este natus error sit volutate accusantium dolor laudant totam rem aperiam eaupsa abillo inven veritatis</p>
  </div>
  <svg class="abs" style="left:1066px;top:2301px;top:-1px" width="0" height="0"></svg>
  <div class="abs" style="left:1066px;top:304px;width:42px;height:42px;border-radius:50%;background:var(--blue);display:flex;align-items:center;justify-content:center">
    <svg width="20" height="20" viewBox="0 0 20 20"><path d="M4 16c0-6 4-9 10-9M10 3l5 4-5 4" fill="none" stroke="#fff" stroke-width="2.2"/></svg>
  </div>
</section>

<!-- Pricing -->
<h2 class="abs heading" style="top:2911px">Choose <span>Pricing</span> Plans</h2>
<p class="abs lead" style="top:2966px">Discover why users love our app. Read real-life experiences and see how our virtual<br>assistant is simplifying daily tasks.</p>

<div class="plan" style="left:112px">
  <div class="plan-head" style="background:linear-gradient(90deg,#1a62e6,#2f82f5)"></div>
  <div class="plan-name">Basic Plan</div>
  <div class="plan-price"><sup>$</sup>399</div>
  <div class="plan-tag" style="color:var(--blue)">Monthly</div>
  <ul>
    <li><span class="ok"></span>Email Support</li>
    <li><span class="ok"></span>Free Upgrades system</li>
    <li><span class="no"></span>Real-life experiences</li>
    <li><span class="no"></span>Your text is here</li>
  </ul>
  <a class="btn">Buy Now</a>
</div>
<div class="plan" style="left:445px">
  <div class="plan-head" style="background:linear-gradient(90deg,#f7a43a,#fbc54a)"></div>
  <div class="plan-name">Premimum Plan</div>
  <div class="plan-price"><sup>$</sup>1099</div>
  <div class="plan-tag" style="color:var(--orange)">Annual</div>
  <ul>
    <li><span class="ok"></span>Email Support</li>
    <li><span class="ok"></span>Free Upgrades system</li>
    <li><span class="ok"></span>Real-life experiences</li>
    <li><span class="ok"></span>Your text is here</li>
  </ul>
  <a class="btn">Buy Now</a>
</div>
<div class="plan" style="left:779px">
  <div class="plan-head" style="background:linear-gradient(90deg,#0e2f95,#1843b8)"></div>
  <div class="plan-name">Advance Plan</div>
  <div class="plan-price"><sup>$</sup>599</div>
  <div class="plan-tag" style="color:var(--navy)">Monthly</div>
  <ul>
    <li><span class="ok"></span>Email Support</li>
    <li><span class="ok"></span>Free Upgrades system</li>
    <li><span class="ok"></span>Real-life experiences</li>
    <li><span class="no"></span>Your text is here</li>
  </ul>
  <a class="btn">Buy Now</a>
</div>

<!-- News -->
<section class="section" style="top:3520px;height:571px;background:linear-gradient(180deg,#ffffff,#f3f7ff)"></section>
<h2 class="abs heading" style="top:3566px">Latest <span>News</span></h2>
<p class="abs lead" style="top:3619px">Discover why users love our app. Read real-life experiences and see how our virtual<br>assistant is simplifying daily tasks.</p>

<article class="news" style="left:112px">
  <div class="news-img" role="img" aria-label="Photo of a dim data operations room with glowing screens" style="background:linear-gradient(135deg,#1c2a44,#3d6aa8)"></div>
  <div class="news-date">Monday 25 April, 2023</div>
  <h3 class="news-title">Miscovery incommode earnestly commanded if.</h3>
  <div class="news-more">Continue Reading <svg width="18" height="10" viewBox="0 0 18 10"><path d="M0 5h16M12 1l4 4-4 4" fill="none" stroke="#1a62e6" stroke-width="1.5"/></svg></div>
</article>
<article class="news" style="left:444px">
  <div class="news-img" role="img" aria-label="Photo of hands on a tablet with a glowing network diagram" style="background:linear-gradient(135deg,#0b1736,#2250a8)"></div>
  <div class="news-date">Monday 25 April, 2023</div>
  <h3 class="news-title">Expression acceptance imprudence particular</h3>
  <div class="news-more">Continue Reading <svg width="18" height="10" viewBox="0 0 18 10"><path d="M0 5h16M12 1l4 4-4 4" fill="none" stroke="#1a62e6" stroke-width="1.5"/></svg></div>
</article>
<article class="news" style="left:775px">
  <div class="news-img" role="img" aria-label="Photo of a person working at a desktop computer in an office" style="background:linear-gradient(135deg,#c8d3e0,#5a6f8c)"></div>
  <div class="news-date">Monday 25 April, 2023</div>
  <h3 class="news-title">Considered imprudence of technical friendship.</h3>
  <div class="news-more">Continue Reading <svg width="18" height="10" viewBox="0 0 18 10"><path d="M0 5h16M12 1l4 4-4 4" fill="none" stroke="#1a62e6" stroke-width="1.5"/></svg></div>
</article>

<!-- Footer -->
<footer class="section footer">
  <div class="abs" style="left:110px;top:62px">
    <div class="brand"><span class="brand-dot"></span>Clearpath Ledgers</div>
    <div class="tagline" style="margin-top:6px;margin-left:6px">Empowering Healthcare</div>
  </div>
  <p class="abs" style="left:112px;top:148px;width:250px;font-size:13px;line-height:26px;color:var(--muted)">Amet minim mollit non deserunt ullamco est sit aliqua dolor do amet sint. Velit officia consequat</p>

  <div class="f-head" style="left:449px">Company</div>
  <ul class="f-links" style="left:452px"><li>About Us</li><li>Privacy Policy</li><li>Terms &amp; Conditions</li><li>Contact</li></ul>

  <div class="f-head" style="left:681px">Resource</div>
  <ul class="f-links" style="left:681px"><li>Products</li><li>Pricing</li><li>FAQ</li><li>Careers</li></ul>

  <div class="f-head" style="left:865px">Address</div>
  <ul class="f-links" style="left:865px">
    <li style="display:flex;gap:20px;align-items:center"><svg width="16" height="12" viewBox="0 0 16 12"><rect width="16" height="12" rx="2" fill="#1a62e6"/><path d="M1 1l7 6 7-6" fill="none" stroke="#fff" stroke-width="1.4"/></svg>hello@clearpathledgers.example</li>
    <li style="display:flex;gap:20px;align-items:center;height:40px"><svg width="16" height="16" viewBox="0 0 16 16"><path d="M3 1l3 3-2 2c1 2 3 4 5 5l2-2 3 3-2 3C7 15 1 9 1 3z" fill="#1a62e6"/></svg>+1 555 014 2290</li>
  </ul>

  <p class="abs" style="left:115px;top:293px;font-size:11px;color:var(--muted)">Copyright @2023 Clearpath Ledgers.com</p>
</footer>

</body>
</html>
```